Veltarum

Standard Business Card design.
Sample two-sided design uploaded. White front, Black back.
Would like white shield to be on all black background side.
Willing to look at a couple creative designs, but nothing crazy.
Preference for a classic, confident, strong design.

```html
<!DOCTYPE html>
<html lang="en">
<head>
<meta charset="UTF-8">
<title>Veltarum Business Card</title>
<link href="https://fonts.googleapis.com/css2?family=Montserrat:wght@600&family=Arimo:wght@400;700&display=swap" rel="stylesheet">
<style>
  :root {
    --backdrop: #8a8a8a;
    --card: #121212;
    --ink: #ffffff;
    --ink-soft: #e6e6e6;
  }
  * { box-sizing: border-box; margin: 0; padding: 0; }
  html, body {
    width: 1200px; height: 960px; overflow: hidden;
    background: var(--backdrop);
  }
  .canvas { position: relative; width: 1200px; height: 960px; }
  .card {
    position: absolute; width: 700px; height: 400px;
    background: var(--card); border-radius: 28px; overflow: hidden;
    color: var(--ink);
  }
  .card--front { left: 110px; top: 70px; }
  .card--back { left: 390px; top: 490px; }

  .brand-name {
    font-family: "Montserrat", sans-serif; font-weight: 600;
    color: var(--ink); letter-spacing: 0.12em; text-transform: uppercase;
  }
  .card--front .brand-name {
    position: absolute; left: 0; right: 0; top: 160px;
    text-align: center; font-size: 72px;
  }
  .card--back .brand-name {
    position: absolute; left: 20px; width: 420px; top: 150px;
    text-align: center; font-size: 52px;
  }
  .divider {
    position: absolute; left: 462px; top: 60px; width: 1px; height: 240px;
    background: var(--ink-soft);
  }
  .contact {
    position: absolute; left: 486px; top: 64px;
    font-family: "Arimo", sans-serif; color: var(--ink-soft); font-size: 15px;
  }
  .contact__name { font-weight: 700; font-size: 22px; color: var(--ink); }
  .contact__role { margin-top: 4px; }
  .contact__address { margin-top: 24px; line-height: 1.45; }
  .contact__list { list-style: none; margin-top: 16px; }
  .contact__list li { display: flex; align-items: center; gap: 10px; line-height: 1.6; }
  .contact__list svg { width: 13px; height: 13px; flex: none; }
  .band {
    position: absolute; left: 0; right: 0; top: 332px; height: 20px;
    background: var(--ink);
  }
  .band-mark {
    position: absolute; right: 28px; top: 308px;
    font-family: "Montserrat", sans-serif; font-weight: 600;
    font-size: 12px; letter-spacing: 0.12em; color: var(--ink);
  }
</style>
</head>
<body>
<div class="canvas">
  <section class="card card--front">
    <div class="brand-name">Veltarum</div>
  </section>

  <section class="card card--back">
    <div class="brand-name">Veltarum</div>
    <div class="divider"></div>
    <div class="contact">
      <div class="contact__name">MARTEN HALE</div>
      <div class="contact__role">Director</div>
      <div class="contact__address">PO Box 4410,<br>Greenport, NY 11944</div>
      <ul class="contact__list">
        <li>
          <svg viewBox="0 0 16 16" fill="#fff"><path d="M3.6 1.5l2.3 2.6-1.3 1.8c.9 2 2.5 3.6 4.5 4.5l1.8-1.3 2.6 2.3-1.4 2.1C7.4 13.4 2.6 8.6 1.5 3z"/></svg>
          555 204 318
        </li>
        <li>
          <svg viewBox="0 0 16 16" fill="#fff"><rect x="1" y="3" width="14" height="10" rx="1"/><path d="M1.5 3.5L8 9l6.5-5.5" stroke="#121212" stroke-width="1.4" fill="none"/></svg>
          info@veltarum.com
        </li>
        <li>
          <svg viewBox="0 0 16 16" fill="none" stroke="#fff" stroke-width="1.4"><circle cx="8" cy="8" r="6.5"/><ellipse cx="8" cy="8" rx="2.8" ry="6.5"/><path d="M1.5 8h13"/></svg>
          www.veltarum.com
        </li>
      </ul>
    </div>
    <div class="band-mark">VELTARUM</div>
    <div class="band"></div>
  </section>
</div>
</body>
</html>
```